Business Card for: Keelwright Financial Advisory Services Inc.

provide strategic financial advisory services to companies in the areas of corporate finance, mergers and acquisitions, executive coaching and strategic planning

Target Market(s)

Companies, banks, accountants, lawyers

Industry/Entity Type

High end business consulting in corporate finance, mergers and acquisitions, consulting

Contact Information for Business Card

Name of company, Name: xxxxxx xxxxxx , CEO, - phone number: 1-xxx-xxx-xxxx, - email address,

Requirements
Must have
• Must be professional and simple.
Nice to have
• simple, straight graphics, must give the impression that we are trustworthy, professional, competent
Should not have
• loud colors, loud design features

```html
<!DOCTYPE html>
<html lang="en">
<head>
<meta charset="utf-8">
<title>Keelwright Financial Advisory – Business Card</title>
<link href="https://fonts.googleapis.com/css2?family=Montserrat:wght@400;500;700;800&display=swap" rel="stylesheet">
<style>
  :root {
    --backdrop: #cccccc;
    --navy: #133a60;
    --sky: #1ea0dc;
    --paper: #ffffff;
    --ink: #2b2b2b;
    --rule: #8a93a6;
  }
  * { margin: 0; padding: 0; box-sizing: border-box; }
  html, body {
    width: 1146px; height: 1200px; overflow: hidden;
    background: var(--backdrop);
    font-family: "Montserrat", sans-serif;
  }
  .canvas { position: relative; width: 1146px; height: 1200px; }

  .card { position: absolute; left: 228px; width: 690px; }
  .card-front { top: 174px; height: 401px; background: var(--navy); }
  .card-back  { top: 632px; height: 394px; background: var(--paper); }

  .brand-name {
    position: absolute; left: 0; right: 0; text-align: center;
    font-weight: 700; text-transform: uppercase; white-space: nowrap;
  }
  .card-front .brand-name { color: var(--paper); }
  .card-front .brand-primary { top: 182px; font-size: 48px; letter-spacing: 1px; }
  .card-front .brand-secondary { top: 248px; font-size: 27px; }

  .back-brand { position: absolute; left: 40px; width: 336px; top: 0; height: 100%; }
  .card-back .brand-name { color: var(--navy); }
  .card-back .brand-primary { top: 200px; font-size: 33px; letter-spacing: 0.5px; }
  .card-back .brand-secondary { top: 248px; font-size: 16.5px; }

  .divider {
    position: absolute; left: 342px; top: 101px; width: 1px; height: 177px;
    background: var(--rule);
  }

  .contact-block { position: absolute; left: 367px; top: 114px; }
  .person-name { font-weight: 700; font-size: 24px; letter-spacing: 0.5px; color: var(--navy); text-transform: uppercase; line-height: 1; }
  .person-name .surname { color: var(--sky); }
  .person-role { margin-top: 8px; font-size: 16px; color: var(--ink); }

  .contact-list { list-style: none; margin-top: 25px; }
  .contact-list li {
    display: flex; align-items: center; height: 26px;
    font-size: 16px; color: var(--ink);
  }
  .contact-list svg { width: 16px; height: 16px; margin-right: 7px; fill: var(--navy); flex: none; }

  .address {
    position: absolute; left: 0; right: 0; top: 334px; text-align: center;
    font-size: 16px; color: var(--ink);
  }
</style>
</head>
<body>
<div class="canvas">

  <section class="card card-front">
    <div class="brand-name brand-primary">Keelwright</div>
    <div class="brand-name brand-secondary">Financial Advisory Inc.</div>
  </section>

  <section class="card card-back">
    <div class="back-brand">
      <div class="brand-name brand-primary">Keelwright</div>
      <div class="brand-name brand-secondary">Financial Advisory Inc.</div>
    </div>

    <div class="divider"></div>

    <div class="contact-block">
      <div class="person-name">Marcus <span class="surname">Ellery</span></div>
      <div class="person-role">Founder &amp; CEO</div>
      <ul class="contact-list">
        <li>
          <svg viewBox="0 0 24 24" aria-hidden="true"><path d="M6.6 10.8a15.1 15.1 0 0 0 6.6 6.6l2.2-2.2c.3-.3.7-.4 1-.2 1.1.4 2.3.6 3.6.6.6 0 1 .4 1 1V20c0 .6-.4 1-1 1A17 17 0 0 1 3 4c0-.6.4-1 1-1h3.5c.6 0 1 .4 1 1 0 1.3.2 2.5.6 3.6.1.3 0 .7-.2 1z"/></svg>
          +33 6 41 58 27 90
        </li>
        <li>
          <svg viewBox="0 0 24 24" aria-hidden="true"><path d="M2 5h20v14H2z" fill="none"/><path d="M2 5h20v2l-10 6L2 7zM2 9l10 6 10-6v10H2z"/></svg>
          info@keelwrightfinancialinc.com
        </li>
        <li>
          <svg viewBox="0 0 24 24" aria-hidden="true"><circle cx="12" cy="12" r="10"/><path d="M2 12h20M12 2c3 3 3 17 0 20M12 2c-3 3-3 17 0 20" stroke="#fff" stroke-width="1.4" fill="none"/></svg>
          www.keelwrightfinancialinc.com
        </li>
      </ul>
    </div>

    <div class="address">2150 Harbor Crest Avenue Washington, DC 20016</div>
  </section>

</div>
</body>
</html>
```